Brellin Trade Partners - we are Asian sourcing agents

We are sourcing agents based in the USA and we act as sourcing agents for clients in throughout the world. We focus primarily on custom sewn goods. So basically companies who do not have the in-house expertise to do it themselves, come to us and have us find suitable factories in Asia to do the production. We are middlemen. We find the factories...quote the project...manage the quality control and then deliver the goods directly to our customer's door. We pride ourselves in making the communication very easy and precise.

Current page is www.brellintrade.example

I am not happy w/ the overall look. The spacing...the photos, the fonts...the design elements...the pictures. I want a cool, crisp design that conveys professionalism and clearly depicts/explains what we do.

Requirements
Must have
• use my logo....I like it...it was designed by someone on this website.
Nice to have
• a video/animation of the entire process would be wonderful. Showing initial contact with our office in the USA...then to my correspondence with my offices in Taiwan and in Hong Kong...and then back and fort w/ the customer.....and then between my people in Hong Kong/Taiwan with the local factories......and then a quote is generated and sent to my client......to samples being made and sent for approval.....to a PO being generated......to final samples being sent.....to the order being shipped and delivered to the clients warehouse. I was thinking of an animation showing arrows and text showing the back and forth communication and explaining how the process flows.

```html
<!DOCTYPE html>
<html lang="en">
<head>
<meta charset="utf-8">
<title>Brellin Trade Partners – Asian Sourcing Agents</title>
<link rel="stylesheet" href="https://fonts.googleapis.com/css2?family=Cabin:wght@400;500;600&family=Open+Sans:wght@400;600;700&display=swap">
<style>
:root{
  --green:#6b8a16;
  --green-dark:#3f5510;
  --navy:#0e1552;
  --navy-deep:#0a0f3e;
  --ink:#1d1d1d;
  --text:#555;
  --soft:#f2f2f2;
  --line:#c9c9c9;
  --white:#fff;
}
*{margin:0;padding:0;box-sizing:border-box}
html,body{width:730px;height:1200px;overflow:hidden;background:var(--white)}
body{position:relative;font-family:"Cabin",sans-serif;color:var(--ink)}
.abs{position:absolute}

/* Header */
.site-header{position:absolute;left:0;top:0;width:730px;height:56px;background:var(--white)}
.brand{position:absolute;left:56px;top:17px;font-family:"Open Sans",sans-serif;font-weight:700;font-size:15px;color:var(--navy);letter-spacing:.2px;display:flex;align-items:center;gap:6px}
.brand-mark{width:10px;height:10px;background:var(--green)}
.nav{position:absolute;top:27px;font-family:"Open Sans",sans-serif;font-size:8px;color:#222;letter-spacing:.2px}
.nav-quote{position:absolute;left:584px;top:21px;width:93px;height:21px;background:var(--green);color:var(--white);font-family:"Open Sans",sans-serif;font-size:8px;display:flex;align-items:center;justify-content:center;letter-spacing:.2px}

/* Hero */
.hero{position:absolute;left:0;top:56px;width:730px;height:316px;background:radial-gradient(ellipse at 30% 45%,#2f6fc4 0%,#16396f 35%,#0b1a36 70%,#070d1c 100%)}
.hero-title{position:absolute;left:380px;top:116px;width:300px;text-align:center;font-family:"Open Sans",sans-serif;font-weight:700;font-size:15.5px;line-height:21px;color:var(--white);letter-spacing:.4px}
.hero-arrow{position:absolute;top:147px}

/* Intro */
.intro{position:absolute;left:0;top:372px;width:730px;height:118px;background:var(--soft);text-align:center}
.intro h1{font-weight:400;font-size:16px;color:#333;margin-top:19px}
.intro p{width:592px;margin:12px auto 0;font-size:8.2px;line-height:12px;color:var(--text)}

/* How it works */
.how-title{left:59px;top:521px;font-size:15px;font-weight:400;color:#333}
.how-sub{left:59px;top:545px;font-size:12px;font-weight:400;color:#222}
.how-text{left:60px;top:572px;width:314px;font-size:8.2px;line-height:11.8px;color:var(--text)}
.btn{position:absolute;background:var(--green);color:var(--white);font-family:"Open Sans",sans-serif;display:flex;align-items:center;justify-content:center}
.btn-read{left:60px;top:665px;width:88px;height:24px;font-size:8.5px;font-weight:600}
.video{left:404px;top:519px;width:267px;height:145px;background:linear-gradient(135deg,#9a9a9a,#5a5a5a 55%,#2e2e2e)}
.video-play{position:absolute;left:122px;top:61px;width:24px;height:22px;background:var(--green)}
.player{left:404px;top:667px;width:267px;height:23px;display:flex;align-items:center;font-family:"Open Sans",sans-serif;font-size:6px;color:#888}
.player-btn{width:23px;height:23px;background:var(--navy);display:flex;align-items:center;justify-content:center;margin-right:6px}
.track{width:120px;height:3px;background:#aaa;margin:0 7px;position:relative}
.track i{position:absolute;left:0;top:0;height:3px;width:80px;background:#444}

/* Products */
.products-title{left:0;top:744px;width:730px;text-align:center;font-size:15px;font-weight:400;color:#222}
.product{position:absolute;top:784px;width:116px}
.product-img{width:116px;height:102px;border:1px solid var(--line)}
.product-name{text-align:center;font-size:10px;color:#333;margin-top:7px}
.dots{left:352px;top:919px;display:flex;gap:4px}
.dots span{width:4px;height:4px;border-radius:50%;background:#ccc}
.dots span:first-child{background:var(--navy)}

/* Call to action */
.cta{position:absolute;left:0;top:958px;width:730px;height:56px;background:var(--green);color:var(--white)}
.cta h2{position:absolute;left:56px;top:11px;font-weight:400;font-size:14px}
.cta p{position:absolute;left:59px;top:34px;font-family:"Open Sans",sans-serif;font-size:7.2px}
.cta-btn{position:absolute;left:497px;top:16px;width:165px;height:23px;background:var(--green-dark);font-size:11px;display:flex;align-items:center;justify-content:center}

/* Footer */
.footer{position:absolute;left:0;top:1014px;width:730px;height:150px;background:var(--navy);color:#dfe2f0;font-family:"Open Sans",sans-serif}
.footer h3{position:absolute;top:23px;font-size:7.5px;font-weight:600;color:var(--white)}
.footer-text{position:absolute;font-size:6.5px;line-height:8.8px;color:#cfd3e6}
.links{position:absolute;left:238px;top:40px;list-style:none;font-size:6.5px;line-height:12px}
.links li::before{content:"";display:inline-block;width:3px;height:3px;border-radius:50%;background:#cfd3e6;margin:0 8px 1px 2px}
.more{position:absolute;left:158px;top:105px;font-size:7px;color:#8c93b8;display:flex;align-items:center;gap:3px}
.contact-row{position:absolute;left:373px;font-size:6.5px;line-height:11.5px;display:flex;gap:7px}
.field{position:absolute;left:548px;width:120px;height:16px;background:#1e2a6e;border:1px solid #2c3880;font-size:6px;color:#cfd3e6;padding:3px 5px;display:flex;justify-content:space-between;align-items:center}
.contact-btn{position:absolute;left:622px;top:118px;width:46px;height:12px;background:var(--green);color:var(--white);font-size:6.5px;font-weight:600;display:flex;align-items:center;justify-content:center}
.bottom-bar{position:absolute;left:0;top:1164px;width:730px;height:36px;background:var(--navy-deep);font-family:"Open Sans",sans-serif;font-size:6.5px;color:#dfe2f0}
.bottom-bar p{position:absolute;left:60px;top:13px}
.social{position:absolute;left:608px;top:13px;display:flex;gap:9px}
.social span{width:9px;height:9px;border-radius:50%;background:#dfe2f0}
</style>
</head>
<body>

<header class="site-header">
  <div class="brand"><span class="brand-mark"></span>Brellin Trade Partners</div>
  <span class="nav" style="left:288px">HOME</span>
  <span class="nav" style="left:339px">PRODUCT CATEGORIES</span>
  <span class="nav" style="left:453px">ABOUT US</span>
  <span class="nav" style="left:521px">CONTACT US</span>
  <div class="nav-quote">REQUEST QUOTE</div>
</header>

<section class="hero" role="img" aria-label="Glowing dotted world map held above an open hand on a deep blue background">
  <svg class="hero-arrow" style="left:12px" width="22" height="22" viewBox="0 0 22 22"><circle cx="11" cy="11" r="9.5" fill="none" stroke="#8a97ad" stroke-width="1.4"/><path d="M13 6.5 L8 11 L13 15.5Z" fill="#8a97ad"/></svg>
  <svg class="hero-arrow" style="left:694px" width="22" height="22" viewBox="0 0 22 22"><circle cx="11" cy="11" r="9.5" fill="none" stroke="#8a97ad" stroke-width="1.4"/><path d="M9 6.5 L14 11 L9 15.5Z" fill="#8a97ad"/></svg>
  <h2 class="hero-title">WE ARE HELPING TO OUTSOURCE ASIAN INTO WORK ACROSS THE COUNTRY</h2>
</section>

<section class="intro">
  <h1>Sourcing custom goods in China</h1>
  <p>We outsource sewing services direct from China. Our long-established and extensive network of offshore factory-partners provides our clients with access to a wide variety of contract sewing expertise from Chinese manufacturers. Clients only need to communicate with our US agents, but will have the benefits of the cost savings &amp; quality workmanship from offshore outsourcing from Asia.</p>
</section>

<h2 class="abs how-title">How It Works</h2>
<h3 class="abs how-sub">Lorem ipsum dolor sit amet, consectetur adipiscing elit.</h3>
<p class="abs how-text">Etiam faucibus aliquam nunc in convallis. Donec erat magna, dapibus sit amet dolor eu, convallis suscipit nisi. Integer rhoncus blandit mi vitae molestie. Aenean sed nisi eleifend, luctus nunc ut, facilisis mi. Integer quam odio, ullamcorper sit amet molestie bibendum Lorem ipsum dolor sit amet, consectetur adipiscing elit. Cras rhoncus vitae lectus non venenatis. Vestibulum id laoreet velit.</p>
<div class="btn btn-read">Read More</div>

<div class="abs video" role="img" aria-label="Black and white video still of a business team in suits">
  <div class="video-play"><svg width="24" height="22" viewBox="0 0 24 22"><path d="M10 7 L15 11 L10 15Z" fill="#fff"/></svg></div>
</div>
<div class="abs player">
  <div class="player-btn"><svg width="8" height="8" viewBox="0 0 8 8"><path d="M2 1 L7 4 L2 7Z" fill="#fff"/></svg></div>
  <span>00:15:35</span>
  <div class="track"><i></i></div>
  <span>2:15:35</span>
  <svg style="margin-left:5px" width="8" height="7" viewBox="0 0 8 7"><path d="M0 2h2l3-2v7L2 5H0Z" fill="#888"/></svg>
  <svg style="margin-left:4px" width="18" height="6" viewBox="0 0 18 6"><g fill="#2aa6a6"><rect x="0" width="1.2" height="6"/><rect x="2.5" width="1.2" height="6"/><rect x="5" width="1.2" height="6"/><rect x="7.5" width="1.2" height="6"/></g><g fill="#aaa"><rect x="10" width="1.2" height="6"/><rect x="12.5" width="1.2" height="6"/><rect x="15" width="1.2" height="6"/></g></svg>
  <svg style="margin-left:10px" width="9" height="8" viewBox="0 0 9 8"><rect x=".5" y=".5" width="8" height="7" fill="none" stroke="#888"/><rect x="2.5" y="2.5" width="4" height="3" fill="#888"/></svg>
</div>

<h2 class="abs products-title">Some of our products</h2>
<div class="product" style="left:60px"><div class="product-img" role="img" aria-label="Sewing machine stitching red fabric" style="background:linear-gradient(135deg,#d9d9d9,#b24a3a 55%,#c4161c)"></div><p class="product-name">Sewn Goods</p></div>
<div class="product" style="left:184px"><div class="product-img" role="img" aria-label="Black and red messenger bag" style="background:radial-gradient(ellipse at center,#4a4a4a 0%,#6a6a6a 35%,#fff 70%)"></div><p class="product-name">Sewn Goods</p></div>
<div class="product" style="left:308px"><div class="product-img" role="img" aria-label="Pair of grey and black winter gloves" style="background:radial-gradient(ellipse at center,#c9c9c9 0%,#e2e2e2 40%,#fff 70%)"></div><p class="product-name">Sewn Goods</p></div>
<div class="product" style="left:431px"><div class="product-img" role="img" aria-label="Navy and silver motorcycle cover" style="background:radial-gradient(ellipse at center,#1d2a6e 0%,#5a6595 40%,#fff 72%)"></div><p class="product-name">Sewn Goods</p></div>
<div class="product" style="left:555px"><div class="product-img" role="img" aria-label="Quilted cushion pad with blue base" style="background:radial-gradient(ellipse at center,#d6dcef 0%,#a9c0e6 40%,#fff 72%)"></div><p class="product-name">Sewn Goods</p></div>
<div class="abs dots"><span></span><span></span><span></span><span></span></div>

<section class="cta">
  <h2>Outsource Your Sewing Needs to Trusted Contractors in China</h2>
  <p>Please contact us for immediate consultation regarding your outsourcing project.</p>
  <div class="cta-btn">Request Quote</div>
</section>

<footer class="footer">
  <h3 style="left:60px">WHO WE ARE</h3>
  <p class="footer-text" style="left:60px;top:41px;width:130px">Lorem ipsum dolor sit amet, consectetur adipiscing elit. Nullam venenatis velit blandit est condimentum aliquet. Curabitur ut libero justo. Nulla ut ex facilisis, tincidunt quam vitae, iaculis orci. Nullam eu faucibus nibh.</p>
  <div class="more">More <svg width="9" height="9" viewBox="0 0 9 9"><circle cx="4.5" cy="4.5" r="4" fill="none" stroke="#8c93b8" stroke-width=".8"/><path d="M2.5 4.5h4M5 3l1.5 1.5L5 6" fill="none" stroke="#8c93b8" stroke-width=".8"/></svg></div>

  <h3 style="left:238px">USEFUL LINKS</h3>
  <ul class="links">
    <li>CUSTOM BAGS</li><li>CUSTOM CASES</li><li>CUSTOM COVERS</li><li>CUSTOM GLOVES</li><li>CUSTOM SEWN GOODS</li><li>CUSTOM SPORTING GOODS</li>
  </ul>

  <h3 style="left:371px">GET IN TOUCH</h3>
  <p class="footer-text" style="left:372px;top:41px;width:130px">Doloreiur quia commolu ptatemp dolupta oreprerum tibusam eumenis et consent accullignis dentibea</p>
  <div class="contact-row" style="top:75px"><svg width="6" height="8" viewBox="0 0 6 8"><path d="M3 0a3 3 0 0 1 3 3c0 2-3 5-3 5S0 5 0 3a3 3 0 0 1 3-3z" fill="#cfd3e6"/><circle cx="3" cy="3" r="1" fill="#0e1552"/></svg><span>Brellin Trade Partners, LLC<br>14 Harbor Lane, Suite 3<br>Easton, NH 03000</span></div>
  <div class="contact-row" style="top:120px"><svg width="7" height="7" viewBox="0 0 7 7"><path d="M1.5 0L3 1.8 2.2 2.8a4 4 0 0 0 2 2L5.2 4 7 5.5 6 7C3 7 0 4 0 1z" fill="#cfd3e6"/></svg><span>Tel: 555-014-2290, Fax: 555-014-2291</span></div>
  <div class="contact-row" style="top:132px"><svg width="7" height="6" viewBox="0 0 7 6"><rect width="7" height="6" fill="#cfd3e6"/><path d="M0 0l3.5 3L7 0" fill="none" stroke="#0e1552" stroke-width=".7"/></svg><span>Email: info@brellintrade.example</span></div>

  <h3 style="left:546px">CONTACT</h3>
  <p class="footer-text" style="left:548px;top:41px;width:120px">Doloreiur quia commolu ptatemp dolupta oreprerum</p>
  <div class="field" style="top:69px">Email</div>
  <div class="field" style="top:92px">Contact For <svg width="7" height="4" viewBox="0 0 7 4"><path d="M.5.5l3 3 3-3" fill="none" stroke="#cfd3e6"/></svg></div>
  <div class="contact-btn">CONTACT</div>
</footer>

<div class="bottom-bar">
  <p>© Brellin Trade Partners, LLC. | USA - Hong Kong - Taipei</p>
  <div class="social"><span></span><span></span><span></span><span></span></div>
</div>

</body>
</html>
```